School Communication Email Template

Looking for a designer to create a couple simple email templates that are matching our brand colors and feel. Attached is the default email template that is currently being sent out. Company details can be shared upon request.

Template is to be used within the booking tool we use (snapshot below) and gmail. Template code is in HTML (see screenshot below).
Updates

Template code for website should be in HTML. Sorry if that created confusion.

Target Market(s)

Parents of kids enrolled in our classes

Industry/Entity Type

Kids sport classes

Font styles to use
Serif

Colors
0054AA
0677BA
7BADD7
CADEEF
E8F1F8
FFF300
FFF600
FEFA6F
FFFEC7
FFFEE8

Requirements
Must have
• Consistency with company brand/colors
Nice to have
• Flexibility to be adjusted as needed

```html
<!DOCTYPE html>
<html lang="en">
<head>
<meta charset="utf-8">
<title>Booking Confirmation Email</title>
<link rel="stylesheet" href="https://fonts.googleapis.com/css2?family=Arvo:wght@700&family=Poppins:wght@400;500;600&display=swap">
<style>
  :root {
    --navy: #253d87;
    --sky: #65b8dc;
    --pale: #dff3fc;
    --pale-edge: #c5e6f5;
    --gold: #f7bd2a;
    --amber: #c98a2c;
    --ink: #3a3a3a;
    --rule: #dddddd;
    --white: #ffffff;
  }
  * { box-sizing: border-box; margin: 0; padding: 0; }
  html, body { width: 1200px; height: 3478px; overflow: hidden; }
  body { background: var(--navy); font-family: 'Poppins', sans-serif; color: var(--ink); position: relative; }
  .email { position: absolute; left: 46px; top: 70px; width: 1108px; height: 3342px; background: var(--white); }
  .abs { position: absolute; }

  .brand-mark { left: 130px; top: 110px; width: 200px; height: 200px; border-radius: 50%; background: var(--gold); }
  .brand-name { left: 43px; top: 316px; font-family: 'Poppins', sans-serif; font-weight: 600; font-size: 37px; color: var(--navy); letter-spacing: 0.5px; white-space: nowrap; }

  .sender { left: 646px; top: 112px; }
  .sender-name { font-family: 'Arvo', serif; font-weight: 700; font-size: 31px; color: #333; margin-bottom: 16px; white-space: nowrap; }
  .sender p { font-size: 30px; line-height: 44px; color: #444; white-space: nowrap; }

  .divider { left: 56px; top: 464px; width: 996px; height: 2px; background: var(--rule); }

  .headline { left: 0; top: 538px; width: 1108px; text-align: center; font-family: 'Arvo', serif; font-weight: 700; font-size: 44px; color: var(--navy); }

  .progress { left: 0; top: 655px; overflow: visible; }

  .greeting { left: 28px; top: 938px; font-size: 28px; }
  .greeting b { color: var(--navy); font-weight: 600; }
  .intro { left: 30px; top: 994px; width: 1040px; font-size: 27px; line-height: 44px; }
  .intro b { font-weight: 600; }

  .details { left: 92px; top: 1222px; width: 920px; height: 1152px; border: 3px solid #b9c4d6; }
  .details-title { position: absolute; left: 20px; top: 21px; width: 880px; height: 137px; background: var(--navy); color: var(--white); font-family: 'Arvo', serif; font-weight: 700; font-size: 42px; letter-spacing: 1px; display: flex; align-items: center; justify-content: center; }
  .details-grid { position: absolute; left: 20px; top: 182px; width: 880px; display: grid; grid-template-columns: 424px 424px; column-gap: 32px; row-gap: 14px; }
  .label, .value { height: 104px; display: flex; align-items: center; justify-content: center; text-align: center; }
  .label { background: var(--sky); color: var(--white); font-weight: 600; font-size: 29px; }
  .value { background: var(--pale); border: 3px solid var(--pale-edge); font-size: 27px; color: #444; }

  .changes { left: 30px; top: 2490px; }
  .changes h2 { font-size: 30px; font-weight: 600; color: var(--navy); margin-bottom: 14px; }
  .changes p { font-size: 27px; }
  .manage-link { display: inline-block; margin-top: 26px; font-size: 28px; font-weight: 500; color: var(--sky); text-decoration: none; border-bottom: 2px solid var(--sky); }
  .appointment-id { margin-top: 22px; }
  .appointment-id b { font-weight: 600; }

  .signoff { left: 30px; top: 2788px; }
  .signoff p { font-size: 27px; }
  .signoff strong { display: block; margin-top: 14px; font-size: 30px; font-weight: 600; color: var(--navy); }

  .footer { left: 0; top: 2948px; width: 1108px; height: 213px; background: var(--gold); }
  .footer-col { position: absolute; top: 40px; font-size: 26px; line-height: 44px; color: #333; }
  .footer-col b { font-weight: 600; }
  .footer-left { left: 32px; }
  .footer-right { left: 595px; }

  .social { left: 0; top: 3224px; width: 1108px; }
</style>
</head>
<body>
  <main class="email">
    <div class="abs brand-mark" aria-hidden="true"></div>
    <div class="abs brand-name">COMPANY NAME</div>

    <div class="abs sender">
      <div class="sender-name">YOUR COMPANY NAME</div>
      <p>418 Maple Ridge Dr, Fairview</p>
      <p>Colorado 80000</p>
      <p>(555) 014-2287</p>
    </div>

    <div class="abs divider"></div>

    <h1 class="abs headline">Your Booking has been confirmed</h1>

    <svg class="abs progress" width="1108" height="120" viewBox="0 0 1108 120" aria-hidden="true">
      <line x1="200" y1="60" x2="850" y2="60" stroke="var(--amber)" stroke-width="3"/>
      <circle cx="200" cy="60" r="26" fill="var(--amber)"/>
      <circle cx="881" cy="60" r="30" fill="var(--white)" stroke="var(--amber)" stroke-width="4"/>
      <circle cx="881" cy="60" r="23" fill="var(--gold)"/>
    </svg>

    <p class="abs greeting">Hello <b>Liam Carter</b></p>
    <p class="abs intro">Your Booking confirmed with <b>COMPANY NAME</b>&nbsp; start date: <b>21-02-2023</b> and end date <b>28-02-2023</b>. Please find the details below.</p>

    <section class="abs details">
      <h2 class="details-title">BOOKING DETAILS</h2>
      <div class="details-grid">
        <div class="label">Student First Name</div><div class="label">Student Last Name</div>
        <div class="value">Liam</div><div class="value">Carter</div>
        <div class="label">Appointment Name</div><div class="label">Appointment Service</div>
        <div class="value">name of appointment</div><div class="value">Service Name</div>
        <div class="label">Booking Start Date</div><div class="label">Booking End Date</div>
        <div class="value">21st Feb, 2023</div><div class="value">23rd Feb, 2023</div>
        <div class="label">Appointment Start Time</div><div class="label">Appointment End Time</div>
        <div class="value">Morning 11.00 AM</div><div class="value">Afternoon : 4:30 PM</div>
      </div>
    </section>

    <section class="abs changes">
      <h2>Need to make changes to this appointment?</h2>
      <p>Manage or edit your appointment online through YOUR PORTAL NAME</p>
      <a class="manage-link" href="#">Manage My Appointment</a>
      <p class="appointment-id"><b>Appointmnet ID:</b> ABCD123456</p>
    </section>

    <div class="abs signoff">
      <p>Thanks</p>
      <strong>Your Company Name</strong>
    </div>

    <footer class="abs footer">
      <div class="footer-col footer-left">
        <b>Your Company Name</b><br>418 Maple Ridge Dr, Fairview,<br>Colorado 80000
      </div>
      <div class="footer-col footer-right">
        (555) 014-2287<br>Info@yourcompany.com<br>www.yourcompany.com
      </div>
    </footer>

    <svg class="abs social" width="1108" height="70" viewBox="0 0 1108 70" aria-label="Social links">
      <circle cx="452" cy="33" r="33" fill="var(--navy)"/>
      <circle cx="545" cy="33" r="33" fill="var(--navy)"/>
      <circle cx="657" cy="33" r="33" fill="var(--navy)"/>
    </svg>
  </main>
</body>
</html>
```